Dynamic Website Design For Dynamic Speaker and Business Coach!

Professional Website Design for a for a Professional Business coach, Business trainer, and Speaker.

Note: This is for design only. No coding required. We want to see your ideas for a great website! This will be a FUN design and not boring like others you may work on.

Please let your creative ideas flow. We have given you a ton of info along with videos to help you understand what we are after, however we WANT your creativity to shine through in your designs!

We are a professional company that has run hundreds of crowdsourced projects on multiple platforms. If you participate in this contest (we hope you do) you can expect great video feedback, consistent feedback, and also our guarantee that if we know your website design will not be what we are looking for we will notify you so you don’t waste your time if there is no chance of you winning.

We respect and recognize this is how you make your living and we will not play games. We look forward to an awesome contest and awesome website designs.

Design Brief:

We are looking for a fresh and fun new design for

http://www.brightpath-advisory.net

This individual (Dana Holloway) teaches and trains corporations and businesses in the fields of leadership, sales, communication, business operations etc. Additionally this business teaches and mentors business professionals in a small group level or 1 on 1.

The website needs to convey trust, professionalism, and affluent, while at the same time having some personality!

This business operates on 3 core principles that we would like to see incorporated into the logo if it is a good fit. The 3 principals are:

Focus
Accountability
Results

Here is a video to help explain what we like about the current site and what we don’t like:
http://clipvault.example/t/QwpLmr82kTnb

As you can see the website is geared towards business professionals. Please look over the website to learn what they do. Obviously this is not a good website so we need your help.

We want a website that is professional-looking, has personality and is geared more towards promoting Dana Holloway, the owner of Summit Path Advisory as a Speaker and Business Consultant. The more you can incorporate clean, professional and fun personality elements into the design, the better off you are at winning.

Here are some examples of other sites in their business that have some things we like:

http://velvetcompass.com Please watch video to learn what we like and don’t like:
http://clipvault.example/t/NrtHq7YpLwc

http://tallpinegrowth.com Please watch video to learn what we like and don’t like:
http://clipvault.example/t/J8vDkrWa

http://www.marthaquince.com Please watch video to learn what we like and don’t like:
http://clipvault.example/t/Pz3mx9Rb2Kq

http://www.vantix7.com Please watch video to learn what we like and don’t like:
http://clipvault.example/t/7Gwe4sNhydv

NOTE: We do not want to copy anything outright. We want to learn, model and take their ideas and make them better. We also want to be flexible and take what we like along with your creativity to make an amazing design.

Here is what we are looking for in more specific terms:

Colors: We like the darker blue (not the light blue like the site) and also a burnt orange. I’ve attached her Logo so you can get an idea and feel for the colors.

When looking at colors please know that the current site and look is NOT what we are going for. We are going for a clean and professional look but also a look that is BOLD, FUN, and Vibrant (hence the colors).

Menu: Horizontal. We like bold and easy to read menu items. Don’t make it small and cluttered.

Site Structure: Clean and easy to navigate. We have a lot of content to display so we need a clean structure that breaks up the text and content areas.
Images: Please pull images from the current site. We can always replace the images of course, but if you show them “their own stuff” in the new design you will be closer to winning because it will feel more like “them”

Look and Feel: Professional. Fun. High-End. Business-like. This website needs to convey that Dana Holloway and Summit Path Advisory are professional. That Dana Holloway is a sought-after Speaker and Business Consultant who knows what she is talking about; can be serious when she needs to be, but also likes to have fun with her clients. This site must convey that!

Content Areas: It is a safe bet that if it is on the current site we need it on the new site. So don’t drop anything as it makes it hard to “cut content”.

What we don't want: We do not want clutter, boring, or templates or themes. We don’t want too cartoony, too cute, or too fancy… Be creative!

Out of respect to professional designers who really are working hard to win if you do not follow this brief, you submit worn out themes, templates, or boring designs you will be eliminated. We are offering great prize money for this so we expect great visual designs.
Updates

Project Deadline Extended
Reason: Our client is out of town, and waiting to hear feedback from them. So, in the meantime, we wanted to keep the project going to see what else you designers can come up with. As soon as we hear back from our client, we will pass along the info. Thanks!

Target Market(s)

Target Audience is entrepreneurs and business professionals alike. This is all business to business stuff.

This person teaches and trains startups and billion dollar companies. The common thread is that they are all businesses and companies who need help in various areas including sales, communication, business operations, etc.

Industry/Entity Type

Business

Font styles to use
Sans Serif

Requirements
Must have
• Brief is very detailed. Please review
Nice to have
Should not have

```html
<!DOCTYPE html>
<html lang="en">
<head>
<meta charset="utf-8">
<title>Summit Path Advisory – Business Coach &amp; Speaker</title>
<link rel="stylesheet" href="https://fonts.googleapis.com/css2?family=Open+Sans:ital,wght@0,400;0,600;0,700;1,400;1,700&family=Raleway:ital,wght@0,300;0,400;0,500;1,400&display=swap">
<style>
:root{
  --navy:#123a63;
  --navy-deep:#0d2b4b;
  --orange:#f07126;
  --orange-soft:#f38a45;
  --ink:#2b2b2b;
  --muted:#555;
  --paper:#ffffff;
  --mist:#efefef;
  --stone:#d9d9d9;
  --night:#1d1d1f;
  --night-2:#2a2a2d;
  --sky:#2f7fd6;
}
*{box-sizing:border-box;margin:0;padding:0}
html,body{width:1200px;height:3062px;overflow:hidden}
body{font-family:"Open Sans",Arial,sans-serif;color:var(--ink);background:var(--paper);position:relative}
section,header,nav,footer{position:absolute;left:0;width:1200px}
.abs{position:absolute}

/* header */
.site-header{top:0;height:141px;background:var(--paper)}
.brand{left:440px;top:28px;display:flex;align-items:center;gap:14px}
.brand-dot{width:58px;height:58px;border-radius:50%;background:var(--orange)}
.brand-name{font-family:"Raleway",sans-serif;font-weight:500;font-size:34px;color:var(--navy);line-height:1}
.brand-tag{left:512px;top:94px;font-size:11px;letter-spacing:2px;color:var(--muted);font-weight:600}

/* nav */
.main-nav{top:141px;height:40px;background:var(--navy-deep);display:flex;align-items:center;justify-content:space-between;padding:0 18px}
.main-nav a{color:#fff;text-decoration:none;font-size:14px;font-weight:600;letter-spacing:.3px;white-space:nowrap}

/* hero */
.hero{top:181px;height:389px;background:linear-gradient(90deg,#0f3358,#1c4d7e)}
.video{left:56px;top:20px;width:604px;height:346px;background:linear-gradient(180deg,#5d7fa6,#2b4f79);overflow:hidden}
.video-person{right:60px;top:30px;width:190px;height:280px;background:linear-gradient(180deg,#3a4f70,#22324c);border-radius:90px 90px 0 0}
.video-title{left:18px;top:22px;font-family:"Raleway",sans-serif;font-weight:500;color:#fff;font-size:56px;line-height:62px;text-shadow:0 2px 4px rgba(0,0,0,.4)}
.video-bar{left:0;bottom:0;width:604px;height:34px;background:rgba(10,25,45,.85)}
.hero-copy{left:705px;top:44px;width:450px;color:#fff}
.hero-copy h2{font-size:17px;font-weight:700;margin-bottom:12px}
.hero-copy p{font-size:15px;line-height:23px;color:#d7e2ef}
.btn{position:absolute;left:808px;width:256px;height:46px;border-radius:5px;display:flex;align-items:center;justify-content:center;gap:10px;color:#fff;font-size:14px;font-weight:600;letter-spacing:.5px}
.btn-dark{background:var(--navy-deep);border:1px solid #3e6895}
.btn-orange{background:var(--orange)}
.btn-sky{background:var(--sky)}
.btn i{width:16px;height:16px;border:2px solid #fff;border-radius:50%;display:block}

/* section titles */
.plus{width:28px;height:28px;border:2px solid var(--orange);border-radius:50%;display:inline-flex;align-items:center;justify-content:center;color:var(--orange);font-weight:700;font-size:20px;line-height:1;background:#fff}
.thinking{top:570px;height:276px}
.thinking h2{position:absolute;top:28px;width:1200px;text-align:center;font-family:"Raleway",sans-serif;font-weight:400;font-size:34px;color:var(--ink)}
.thinking h2 .plus{vertical-align:middle;margin-right:18px}
.accent{color:var(--orange)}
.thinking p{position:absolute;left:64px;width:1080px;font-size:17px;line-height:26px;color:var(--ink)}

.coach{top:846px;height:339px;background:var(--mist)}
.coach h2{position:absolute;top:22px;width:1200px;text-align:center;font-family:"Raleway",sans-serif;font-weight:400;font-size:32px;color:var(--ink);line-height:44px}
.coach h2 span{color:var(--orange);display:block;font-size:27px;letter-spacing:.5px}
.arrow-list{position:absolute;list-style:none}
.arrow-list li{position:relative;padding-left:52px;font-size:16px;height:34px;line-height:34px;color:var(--ink);font-weight:600}
.arrow-list li::before{content:"";position:absolute;left:0;top:17px;width:36px;height:1.5px;background:var(--navy)}
.arrow-list li::after{content:"";position:absolute;left:30px;top:13px;width:7px;height:7px;border-top:1.5px solid var(--navy);border-right:1.5px solid var(--navy);transform:rotate(45deg)}
.callout{position:absolute;background:#fff;border:2px solid var(--orange);border-radius:16px;font-size:17px;line-height:25px;color:var(--ink);font-weight:600}
.callout .plus{position:absolute;left:-2px;top:-14px}

/* value */
.value{top:1218px;height:269px}
.value-head{top:0;width:1200px;height:115px;background:var(--stone);text-align:center;padding-top:22px;font-family:"Raleway",sans-serif;font-size:27px;line-height:36px;color:var(--ink)}
.value-head span{color:var(--orange);display:block;font-size:25px}
.value-box{top:115px;height:154px;color:#fff;font-size:16px;line-height:24px;padding:36px 40px 0 30px;font-weight:600}
.value-left{left:0;width:608px;background:var(--navy)}
.value-right{left:620px;width:580px;background:var(--orange)}

/* promise */
.promise{top:1518px;height:392px;background:var(--mist)}
.promise h2{position:absolute;top:32px;width:1200px;text-align:center;font-family:"Raleway",sans-serif;font-weight:500;font-size:26px;color:var(--orange);letter-spacing:.5px}
.promise h3{position:absolute;top:70px;width:1200px;text-align:center;font-family:"Raleway",sans-serif;font-weight:400;font-size:28px;color:var(--ink)}

/* banner */
.banner{top:1910px;height:436px;background:radial-gradient(ellipse at 60% 45%,#55606e 0%,#2c3440 45%,#161b22 100%)}
.portrait{left:93px;top:80px;width:266px;height:266px;border-radius:50%;background:linear-gradient(160deg,#8a6a52,#3b2a22);border:4px solid #4a5462}
.banner .greet{left:526px;top:100px;font-family:"Raleway",sans-serif;font-size:46px;color:#fff;font-weight:400}
.banner .name{left:526px;top:162px;font-family:"Raleway",sans-serif;font-size:62px;color:#fff;font-weight:300;letter-spacing:3px;white-space:nowrap}
.know-more{left:531px;top:264px;width:238px;height:72px;border:1px solid #9aa3ae;border-radius:6px;background:rgba(255,255,255,.12);display:flex;align-items:center;justify-content:center;gap:14px;color:#fff;font-size:17px;font-weight:600;letter-spacing:.5px}
.know-more i{width:22px;height:22px;border:2px solid #fff;border-radius:50%;display:flex;align-items:center;justify-content:center;font-style:normal;font-size:16px;line-height:1}

/* testimonial */
.people{top:2346px;height:351px;background:var(--paper)}
.people h2{top:48px;font-family:"Raleway",sans-serif;font-style:italic;font-weight:400;font-size:40px;color:var(--ink)}
.people h2 b{font-style:normal;font-weight:500}
.client-photo{left:90px;top:136px;width:164px;height:164px;border-radius:50%;background:linear-gradient(180deg,#c9ccd2,#5a6270);border:4px solid #d4d4d4}
.quote{left:308px;top:146px;width:836px;font-size:16px;line-height:23px;color:var(--ink)}
.cite{left:308px;top:280px;font-size:16px;font-weight:700;font-style:italic;color:var(--ink);display:flex;align-items:center;gap:14px}
.cite::before{content:"";width:70px;height:1.5px;background:var(--navy);display:block}

/* footer */
.site-footer{top:2697px;height:365px;background:var(--night)}
.offer{left:20px;top:148px;width:250px;text-align:right;color:#ddd;font-size:14px;line-height:20px}
.offer b{color:#fff;font-size:19px}
.field{position:absolute;border-bottom:1px solid #555;color:#888;font-size:14px;padding-bottom:6px}
.field-area{position:absolute;left:595px;top:42px;width:225px;height:80px;border:1px solid #444;background:var(--night-2);color:#888;font-size:14px;padding:8px}
.send{left:303px;top:175px;width:517px;height:38px;background:var(--night-2);border:1px solid #3a3a3d;color:#fff;font-size:13px;font-weight:600;display:flex;align-items:center;justify-content:center;letter-spacing:1px}
.contact{left:885px;width:290px;display:flex;gap:22px;color:#ccc;font-size:13px;line-height:18px}
.contact svg{flex:none;margin-top:2px}
.contact b{display:block;color:#999;font-size:12px;letter-spacing:1px;font-weight:600}
.contact .big{color:#fff;font-size:17px;font-weight:600}
.copyright{top:283px;width:1200px;text-align:center;color:#aaa;font-size:13px}
.socials{top:322px;left:512px;display:flex;gap:12px}
.socials span{width:22px;height:22px;border-radius:50%;background:#3a3a3e;display:block}
</style>
</head>
<body>

<header class="site-header">
  <div class="brand abs"><span class="brand-dot"></span><span class="brand-name">Summit Path Advisory</span></div>
  <div class="brand-tag abs">FOCUS · ACCOUNTABILITY · RESULTS</div>
</header>

<nav class="main-nav">
  <a>HOME</a><a>PASSION</a><a>WHO WE ARE</a><a>SPEAKER</a><a>FREE VIDEOS</a><a>WEB TV SHOW</a><a>TESTIMONIALS</a><a>MERIDIAN LEARNING</a><a>BLOG</a><a>CONTACT</a>
</nav>

<section class="hero">
  <div class="video abs">
    <div class="video-person abs" role="img" aria-label="Video still of the coach speaking on stage"></div>
    <div class="video-title abs">Do You Need<br>More Focus,<br>Accountability<br>&amp; Results?</div>
    <svg class="abs" style="left:262px;top:150px" width="64" height="70" viewBox="0 0 64 70"><polygon points="32,2 62,19 62,51 32,68 2,51 2,19" fill="#f07126"/><polygon points="24,20 46,35 24,50" fill="#fff"/></svg>
    <svg class="abs" style="left:560px;top:14px" width="28" height="28" viewBox="0 0 28 28"><circle cx="14" cy="14" r="13" fill="rgba(0,0,0,.35)"/><path d="M8 14 L20 8 L16 20 L14 15 Z" fill="#fff"/></svg>
    <div class="video-bar abs">
      <svg width="604" height="34" viewBox="0 0 604 34"><polygon points="14,10 26,17 14,24" fill="#fff"/><text x="38" y="21" fill="#fff" font-size="11" font-family="Open Sans, sans-serif">01:06</text><rect x="82" y="15" width="400" height="4" rx="2" fill="#56657a"/><rect x="82" y="15" width="40" height="4" rx="2" fill="#fff"/><rect x="500" y="12" width="16" height="10" fill="#fff"/><text x="530" y="21" fill="#fff" font-size="11" font-weight="700" font-family="Open Sans, sans-serif">HD</text><rect x="562" y="10" width="18" height="14" fill="none" stroke="#fff" stroke-width="2"/></svg>
    </div>
  </div>
  <div class="hero-copy abs">
    <h2>IS YOUR BUSINESS WORTH THE EFFORT?</h2>
    <p>You’re pouring time, energy, effort, and money into your business. But there’s something missing. And with your help, I can tell you exactly what it is.</p>
  </div>
  <div class="btn btn-dark" style="top:185px"><i></i>FIND OUT NOW</div>
  <div class="btn btn-orange" style="top:251px"><i></i>FREE INSIDER VIDEOS</div>
  <div class="btn btn-sky" style="top:316px"><i></i>UNPLUGGED WEB TV SHOW</div>
</section>

<section class="thinking">
  <h2><span class="plus">+</span>CHANGE YOUR THINKING, <span class="accent">CHANGE YOUR RESULTS!</span></h2>
  <p style="top:108px">Are you searching to bridge the gap between where you are and where you want to be?</p>
  <p style="top:150px">As you face greater pressure to “move the needle” on your company’s productivity and bottom line profitability, how prepared are you to step in and shine as the leader?</p>
  <p style="top:228px">We specialize in guiding leaders to become easier to follow. You’re in the Right Place.</p>
</section>

<section class="coach">
  <h2>Albuquerque Business Coach:<span>FOCUS, ACCOUNTABILITY, &amp; RESULTS</span></h2>
  <ul class="arrow-list" style="left:64px;top:155px">
    <li>Development Of An Operational Plan That Links All Departments</li>
    <li>Implementation And Monitoring Individual And Departmental Plans</li>
    <li>Diagnosing Employee Training Needs</li>
    <li>Delivering The Training To Develop Leaders And Staff</li>
    <li>Coach Leaders, Individuals And Teams</li>
  </ul>
  <div class="callout" style="left:815px;top:128px;width:335px;height:186px;padding:38px 24px 0 30px">
    <span class="plus">+</span>
    Whether you’re leading a company, or are an employee, all of us have a role to play in contributing to the profit and the future of the company.
  </div>
</section>

<section class="value">
  <div class="value-head abs">Your organization expects you to<span>DELIVER VALUE BY DELIVERING RESULTS.</span></div>
  <div class="value-box value-left abs">At Summit Path Advisory, we know as a company or as individuals, clarity of the direction captured in an annual plan that is monitored monthly is one of the surest, quickest and most profitable ways of getting ahead in these challenging times.</div>
  <div class="value-box value-right abs">What is the missing link in your business? What are you searching for? Email me today, conversation is complimentary to investigate where we start building the business you envision for tomorrow.</div>
</section>

<section class="promise">
  <h2>SUMMIT PATH ADVISORY HAS DELIVERED ON OUR PROMISE.</h2>
  <h3>Our clients learn to:</h3>
  <ul class="arrow-list" style="left:64px;top:140px">
    <li>Establish new patterns of productivity for the business</li>
    <li>Clarification of future goals, targets and benchmarks</li>
    <li>Implement actionable steps around short, medium and long-term goals</li>
    <li>Identify roadblocks and disempowering habits</li>
    <li>Create a repeatable process that delivers results</li>
    <li>Transform burned out employees or leaders into fired-up employees</li>
  </ul>
  <div class="callout" style="left:782px;top:123px;width:398px;height:244px;padding:22px 22px 0 26px">
    <span class="plus">+</span>
    With over 25 years of experience in a variety of industries, we know the daily attitudes, habits and goals for successful companies begin with a plan. By training employees where needed and coaching to clear expectations writes success stories daily as the plan unfolds over the course of the year.
  </div>
</section>

<section class="banner">
  <div class="portrait abs" role="img" aria-label="Portrait photo of coach Dana Holloway"></div>
  <div class="greet abs">Here’s to your success!</div>
  <div class="name abs">DANA HOLLOWAY</div>
  <div class="know-more abs"><i>+</i>KNOW MORE</div>
</section>

<section class="people">
  <svg class="abs" style="left:88px;top:62px" width="34" height="30" viewBox="0 0 34 30"><path d="M3 4h20v12H11l-5 5v-5H3z" fill="none" stroke="#e0452a" stroke-width="2.5"/><path d="M14 19h6l6 5v-5h5V9h-5" fill="none" stroke="#e0452a" stroke-width="2.5"/></svg>
  <h2 class="abs" style="left:136px"><span>People</span> <b>SAY:</b></h2>
  <div class="client-photo abs" role="img" aria-label="Photo of client Paul Renner"></div>
  <p class="quote abs">“Dana’s work proved very valuable in the efforts we undertook to pass on to our 280 employees our Vision, and the Values required in order for us to achieve our Vision. Her involvement was always professional, and appreciated by all of us. Without her contribution we would not have been able to progress to the point where we became independently capable of properly describing and implementing the product of the effort we decided to undertake in 2005.”</p>
  <div class="cite abs">Paul Renner - VP and General Manager of Granite Ridge Works</div>
</section>

<footer class="site-footer">
  <div class="offer abs">Sign up for my <b>FREE</b> report “Have Fun While Making Sales” and make more money this month!</div>
  <div class="field" style="left:303px;top:42px;width:280px">Name</div>
  <div class="field" style="left:303px;top:106px;width:280px">Email</div>
  <div class="field-area">Message</div>
  <div class="send abs">SEND</div>
  <div class="contact abs" style="top:50px">
    <svg width="16" height="18" viewBox="0 0 16 18"><path d="M3 1l3 4-2 2c1 3 3 5 6 6l2-2 4 3-2 3C7 17 0 10 1 3z" fill="none" stroke="#999" stroke-width="1.5"/></svg>
    <div><b>CALL US</b><span class="big">505 555-0184</span></div>
  </div>
  <div class="contact abs" style="top:124px">
    <svg width="16" height="20" viewBox="0 0 16 20"><path d="M8 19C3 12 1 9 1 7a7 7 0 0 1 14 0c0 2-2 5-7 12z" fill="none" stroke="#999" stroke-width="1.5"/><circle cx="8" cy="7" r="2.5" fill="#999"/></svg>
    <div><b>ADDRESS</b>4820 Mesa Verde Ave, #210<br>Albuquerque, New Mexico, 87110</div>
  </div>
  <div class="contact abs" style="top:198px">
    <svg width="18" height="14" viewBox="0 0 18 14"><rect x="1" y="1" width="16" height="12" fill="none" stroke="#999" stroke-width="1.5"/><path d="M1 1l8 7 8-7" fill="none" stroke="#999" stroke-width="1.5"/></svg>
    <div><b>SAY HELLO</b>hello@summitpath-advisory.net</div>
  </div>
  <div class="copyright abs">©2014 SUMMIT PATH ADVISORY</div>
  <div class="socials abs"><span></span><span></span><span></span><span></span><span></span><span></span></div>
</footer>

</body>
</html>
```